Web Developer Needs a Business Card Design

I need a personal business card design that represents me as a web developer for potential employers. I would like the background to be a dark color on the front for contrast with my logo and name. The back will have all my information along with a smaller version of the logo. I want something with a modern look and feel, not too conservative. This will be used for potential employers and freelance work.

Industry/Entity Type

Business

Contact Information for Business Card

Front should have my logo and name. The back should have all my personal information which would include: name: Tom Varnuch, phone: 570-614-9083, email: tomvarnuch@mailnest.example, website url: www.tomvarnuch.example, logo, web developer.

Font styles to use
Sans Serif

Requirements
Must have
• Must include my logo. The color palette base color will be the logo color.

```html
<!DOCTYPE html>
<html lang="en">
<head>
<meta charset="utf-8">
<title>Tom Varnuch — Business Card</title>
<link rel="stylesheet" href="https://fonts.googleapis.com/css2?family=Fredoka:wght@600&family=Lato:wght@400;700&display=swap">
<style>
  :root {
    --canvas: #d9d9d9;
    --charcoal-dark: #2c3535;
    --charcoal-light: #6a6f6f;
    --paper: #f7f7f5;
    --teal: #5ccdb2;
    --ink: #2a2a2a;
    --disc-grey: #a9a9a9;
  }
  * { box-sizing: border-box; margin: 0; padding: 0; }
  html, body { width: 1200px; height: 1000px; overflow: hidden; }
  body {
    background: var(--canvas);
    position: relative;
    font-family: "Lato", Arial, sans-serif;
  }
  .card {
    position: absolute;
    top: 350px;
    width: 525px;
    height: 300px;
    border-radius: 3px;
    box-shadow: 0 14px 30px rgba(0,0,0,0.22);
    overflow: hidden;
  }
  .card--front {
    left: 50px;
    background: radial-gradient(ellipse at 50% 40%, var(--charcoal-light) 0%, #454c4c 45%, var(--charcoal-dark) 100%);
  }
  .card--back {
    left: 625px;
    background: var(--paper);
  }
  .brand-disc {
    position: absolute;
    border-radius: 50%;
  }
  .card--front .brand-disc {
    left: 207px;
    top: 40px;
    width: 112px;
    height: 112px;
    background: #3c4444;
    border: 9px solid var(--teal);
    box-shadow: inset 0 4px 10px rgba(0,0,0,0.5);
  }
  .name {
    font-family: "Fredoka", "Arial Rounded MT Bold", sans-serif;
    font-weight: 600;
    color: var(--teal);
    letter-spacing: 1px;
    white-space: nowrap;
  }
  .card--front .name {
    position: absolute;
    left: 0;
    right: 0;
    top: 176px;
    text-align: center;
    font-size: 50px;
  }
  .card--back .name {
    position: absolute;
    left: 36px;
    top: 34px;
    font-size: 44px;
  }
  .role {
    position: absolute;
    left: 40px;
    top: 96px;
    font-family: "Lato", Arial, sans-serif;
    font-weight: 700;
    font-size: 13px;
    letter-spacing: 1px;
    color: var(--ink);
    text-transform: uppercase;
  }
  .card--back .brand-disc {
    left: 40px;
    top: 140px;
    width: 130px;
    height: 130px;
    background: rgba(169,169,169,0.55);
    border: 9px solid rgba(92,205,178,0.7);
  }
  .contact {
    position: absolute;
    left: 196px;
    top: 150px;
    list-style: none;
    font-size: 17px;
    line-height: 34px;
  }
  .contact__label { color: var(--ink); }
  .contact__value { color: var(--teal); }
</style>
</head>
<body>
  <section class="card card--front" aria-label="Card front">
    <div class="brand-disc"></div>
    <h1 class="name">Tom Varnuch</h1>
  </section>

  <section class="card card--back" aria-label="Card back">
    <h2 class="name">Tom Varnuch</h2>
    <p class="role">Logo | Web Developer</p>
    <div class="brand-disc"></div>
    <ul class="contact">
      <li><span class="contact__label">phone</span><span class="contact__value">570-614-9083</span></li>
      <li><span class="contact__label">email</span><span class="contact__value">tomvarnuch@mailnest.example</span></li>
      <li><span class="contact__label">website</span><span class="contact__value">www.tomvarnuch.example</span></li>
    </ul>
  </section>
</body>
</html>
```